BELU Safety Poster

We need a safety poster designed that we can provide to our members to put up on the wall of their factories. It needs to be clear and concise and simple but also that they are aware it is provided by us. We would like the poster to be in line with our branding companies, you can view these on our website www.tarnvalehub.com A3 size please

All files are here https://www.quillstash.com/sh/p8ve2mz7tqs4lr9/QQhuTrwc-LPMaxRuF83Zcf5H1?n=47193052

```html
<!DOCTYPE html>
<html lang="en">
<head>
<meta charset="utf-8">
<title>BELU Safety Poster – Heat Stress</title>
<link rel="stylesheet" href="https://fonts.googleapis.com/css2?family=Alfa+Slab+One&family=Arvo:wght@700&display=swap">
<style>
  :root {
    --frame-dark: #3d3d3d;
    --frame-mid: #4a4a4a;
    --frame-line: #a8a8a8;
    --panel: #9b9b9b;
    --purple: #4a0a88;
    --white: #ffffff;
    --alert: #ff1a00;
    --ink-grey: #555555;
    --ornament: #5a5a5a;
  }
  * { margin: 0; padding: 0; box-sizing: border-box; }
  html, body { width: 849px; height: 1200px; overflow: hidden; background: var(--frame-dark); }
  .poster { position: relative; width: 849px; height: 1200px; background: var(--frame-mid); }
  .poster__frame { position: absolute; inset: 0; }
  .poster__panel {
    position: absolute; left: 72px; top: 72px; width: 706px; height: 1056px;
    background: var(--panel);
  }
  .corner-ornament { position: absolute; width: 30px; height: 30px; border-radius: 50%; background: var(--ornament); }
  .sun-illustration {
    position: absolute; left: 340px; top: 148px; width: 178px; height: 178px;
    border-radius: 50%; background: radial-gradient(circle, #505050 55%, #5c5c5c 56%, #5c5c5c 70%, rgba(90,90,90,0) 71%);
  }
  .heading {
    position: absolute; left: 0; width: 849px; text-align: center;
    font-family: "Alfa Slab One", serif; color: var(--purple); line-height: 1;
  }
  .heading--main { top: 102px; font-size: 40px; }
  .heading--signs { top: 607px; font-size: 45px; }
  .tip {
    position: absolute; font-family: "Arvo", serif; font-weight: 700;
    color: var(--white); font-size: 26px; line-height: 1; white-space: nowrap;
  }
  .tip__drop { position: absolute; left: -28px; top: 0; width: 18px; height: 26px; }
  .divider { position: absolute; left: 174px; top: 576px; width: 508px; height: 16px; }
  .alert-mark {
    position: absolute; left: 166px; top: 858px; width: 30px; height: 86px;
  }
  .alert-text {
    position: absolute; left: 227px; top: 850px; width: 545px;
    font-family: "Arvo", serif; font-weight: 700; color: var(--alert);
    font-size: 20.5px; line-height: 28px;
  }
  .footer-note {
    position: absolute; left: 156px; top: 1017px; width: 190px;
    font-family: "Arvo", serif; font-weight: 700; color: var(--ink-grey);
    font-size: 15.5px; line-height: 20px; text-transform: uppercase;
  }
  .brand-mark {
    position: absolute; left: 362px; top: 962px; width: 140px; height: 128px;
    display: flex; align-items: center; justify-content: center; gap: 8px;
  }
  .brand-mark__dot { width: 18px; height: 18px; border-radius: 50%; background: var(--purple); }
  .brand-mark__name {
    font-family: "Arvo", serif; font-weight: 700; color: var(--purple); font-size: 34px;
  }
  .org-name {
    position: absolute; left: 525px; top: 988px; width: 240px;
    font-family: "Arvo", serif; font-weight: 700; color: var(--ink-grey);
    font-size: 19px; line-height: 20px; text-transform: uppercase;
  }
  .org-name small { font-size: 11px; }
</style>
</head>
<body>
<main class="poster">
  <svg class="poster__frame" width="849" height="1200" viewBox="0 0 849 1200" aria-hidden="true">
    <rect x="22" y="22" width="805" height="1156" fill="var(--frame-dark)"/>
    <g stroke="var(--frame-line)" stroke-width="3" fill="none">
      <line x1="62" y1="41" x2="787" y2="41"/><line x1="62" y1="55" x2="787" y2="55"/>
      <line x1="62" y1="1145" x2="787" y2="1145"/><line x1="62" y1="1159" x2="787" y2="1159"/>
      <line x1="41" y1="62" x2="41" y2="1138"/><line x1="55" y1="62" x2="55" y2="1138"/>
      <line x1="794" y1="62" x2="794" y2="1138"/><line x1="808" y1="62" x2="808" y2="1138"/>
    </g>
  </svg>
  <div class="corner-ornament" style="left:33px;top:33px" role="img" aria-label="corner sun ornament"></div>
  <div class="corner-ornament" style="left:786px;top:33px" role="img" aria-label="corner sun ornament"></div>
  <div class="corner-ornament" style="left:33px;top:1137px" role="img" aria-label="corner sun ornament"></div>
  <div class="corner-ornament" style="left:786px;top:1137px" role="img" aria-label="corner sun ornament"></div>

  <section class="poster__panel" aria-hidden="false"></section>

  <h1 class="heading heading--main">Heat Stress Isn’t Cool</h1>
  <div class="sun-illustration" role="img" aria-label="sun illustration"></div>

  <svg width="0" height="0" style="position:absolute">
    <defs>
      <symbol id="drop" viewBox="0 0 18 26"><path d="M9 1 C12 9 17 13 17 18 A8 8 0 0 1 1 18 C1 13 6 9 9 1Z" fill="var(--purple)"/></symbol>
    </defs>
  </svg>

  <ul class="tips">
    <li class="tip" style="left:167px;top:356px"><svg class="tip__drop"><use href="#drop"/></svg>Drink plenty of water</li>
    <li class="tip" style="left:167px;top:396px"><svg class="tip__drop"><use href="#drop"/></svg>Take breaks</li>
    <li class="tip" style="left:167px;top:436px"><svg class="tip__drop"><use href="#drop"/></svg>Wear light clothing when appropriate</li>
    <li class="tip" style="left:167px;top:476px"><svg class="tip__drop"><use href="#drop"/></svg>Monitor work mates for signs of Heat</li>
    <li class="tip" style="left:115px;top:515px;list-style:none">Stress</li>
  </ul>

  <svg class="divider" viewBox="0 0 508 16" aria-hidden="true">
    <path d="M0 8 L240 5 Q254 2 268 5 L508 8 L268 11 Q254 14 240 11 Z" fill="#3a3a3a"/>
  </svg>

  <h2 class="heading heading--signs">Signs of Heat Exhaustion</h2>

  <ul class="signs" style="list-style:none">
    <li class="tip" style="left:167px;top:688px"><svg class="tip__drop"><use href="#drop"/></svg>Feeling sick, weak or clumsy/dizzy</li>
    <li class="tip" style="left:167px;top:739px"><svg class="tip__drop"><use href="#drop"/></svg>Cramps can also be cause by heat</li>
    <li class="tip" style="left:167px;top:790px"><svg class="tip__drop"><use href="#drop"/></svg>Discomfort from heat rash</li>
  </ul>

  <svg class="alert-mark" viewBox="0 0 30 86" aria-hidden="true">
    <path d="M1 0 H29 L24 58 H6 Z" fill="var(--alert)"/>
    <rect x="3" y="66" width="24" height="18" fill="var(--alert)"/>
  </svg>
  <p class="alert-text">If you have profuse sweating, weakness, nausea or vomiting, headaches and muscle spasms then stop work immediately and seek help</p>

  <p class="footer-note">This is a BELU safety poster</p>
  <div class="brand-mark"><span class="brand-mark__dot"></span><span class="brand-mark__name">BELU</span></div>
  <p class="org-name">Brenwick Elastomer League United <small>Inc</small></p>
</main>
</body>
</html>
```